Software company specialized in data analytics and professional services

We need a landing page design for our business. It should include our logo design. It should have multiple sections :
- stylish head
- what we do (data analytics software, professional services)
- contact form

Target Market(s)

Companies, B2B

Industry/Entity Type

Data

Number of Pages Required

1 page

Font styles to use
Sans Serif

Requirements
Must have
• Dark theme
Should not have
• Gradients on buttons

```html
<!DOCTYPE html>
<html lang="en">
<head>
<meta charset="utf-8">
<title>NORTHGRID – Data Analytics &amp; Professional Services</title>
<link href="https://fonts.googleapis.com/css2?family=Poppins:wght@400;500;600;700&display=swap" rel="stylesheet">
<style>
:root{
  --bg:#140a2b;
  --surface:#1e1140;
  --blob:#221348;
  --band:#2a1656;
  --heading:#f3eefc;
  --text:#bfb6da;
  --muted:#8e85b3;
  --accent:#d44ef0;
  --accent-soft:#b88cff;
  --btn:#c9b8ff;
  --line:#5e5296;
  --card-line:#6b3f8e;
  --footer:#0b0519;
  --white:#fff;
}
*{margin:0;padding:0;box-sizing:border-box}
html,body{width:1200px;height:5147px;overflow:hidden}
body{position:relative;font-family:'Poppins',sans-serif;color:var(--heading);background:var(--bg)}
.abs{position:absolute}
.art{position:absolute;border-radius:24px}
h1,h2,h3{font-weight:500;color:var(--heading)}
p{color:var(--text)}

.hero-bg{left:0;top:0;width:1200px;height:660px}
.logo{left:174px;top:24px;font-size:34px;font-weight:600;color:var(--accent);letter-spacing:1px}
.nav{left:552px;top:32px;display:flex;gap:24px;font-size:14px;font-weight:500;color:var(--accent-soft)}
.hero-title{left:176px;top:200px;font-size:37px;line-height:50px;width:520px}
.hero-text{left:176px;top:312px;width:420px;font-size:11px;line-height:18px;color:var(--text)}

.btn{position:absolute;height:38px;border:2px solid var(--btn);border-radius:20px;font-size:13px;color:var(--btn);display:flex;align-items:center;justify-content:center;font-weight:500;background:transparent}
.btn::after{content:"";position:absolute;right:-22px;top:-4px;width:14px;height:46px;border-left:2px solid var(--btn);border-right:2px solid var(--btn);transform:skewX(-22deg)}
.btn.pink{border-color:var(--accent);color:var(--accent)}
.btn.pink::after{border-color:var(--accent)}

.eyebrow{font-size:12px;color:var(--accent)}
.h-sec{font-size:24px;line-height:34px}
.body-p{font-size:11px;line-height:19px}
.play{display:flex;align-items:center;gap:14px;font-size:13px;color:var(--heading);font-weight:500}
.play i{width:30px;height:30px;border-radius:50%;background:#2f6cf2;position:relative}
.play i::after{content:"";position:absolute;left:12px;top:9px;border-left:10px solid #fff;border-top:6px solid transparent;border-bottom:6px solid transparent}

.check{font-size:11px;color:var(--heading);display:flex;align-items:center;gap:10px}
.check svg{width:14px;height:14px}

.center{left:0;width:1200px;text-align:center}
.card{position:absolute;width:270px;height:302px;border:1.5px dashed var(--card-line);text-align:center;background:var(--surface)}
.card .ic{position:absolute;left:60px;top:28px;width:150px;height:130px;border-radius:50%;background:radial-gradient(circle at 50% 60%,#3a4fa8,#2a2170 60%,var(--surface) 72%)}
.card h3{position:absolute;top:176px;width:100%;font-size:15px}
.card p{position:absolute;top:204px;left:22px;width:226px;font-size:12px;line-height:18px}
.card span{position:absolute;top:256px;width:100%;left:0;font-size:13px;font-weight:600;color:var(--accent)}

.stats{left:174px;top:2648px;width:854px;height:178px;background:var(--band)}
.stat{position:absolute;top:60px;width:200px;text-align:center}
.stat b{display:block;font-size:30px;font-weight:600;line-height:36px;color:var(--heading)}
.stat small{font-size:11px;color:var(--text)}

.post{position:absolute;top:3004px;width:270px;height:358px;border:1px solid #3a2a66;background:var(--surface)}
.post .img{height:240px}
.post .meta{position:absolute;top:258px;left:18px;right:14px;display:flex;justify-content:space-between;font-size:10px;color:var(--text)}
.post .meta i{display:inline-block;width:16px;height:16px;border-radius:50%;background:#4a3e75;vertical-align:middle;margin-right:6px}
.post h3{position:absolute;top:296px;left:18px;width:236px;font-size:13px;line-height:20px;font-weight:600}

.field{position:absolute;border-bottom:1.5px solid var(--line);font-size:12px;color:var(--muted);padding-bottom:14px}

.dots{display:flex;gap:5px;justify-content:center}
.dots i{width:5px;height:5px;border-radius:50%;background:#4a4078}
.dots i.on{background:var(--accent-soft)}

.footer-bg{left:0;top:4750px;width:1200px;height:397px}
.f-logo{left:174px;top:4924px;font-size:28px;font-weight:600;color:#fff;letter-spacing:1px}
.f-text{left:174px;top:4972px;width:240px;font-size:12px;line-height:18px;color:#d9d3ec}
.social{left:174px;top:5026px;display:flex;gap:10px}
.social i{width:20px;height:20px;border-radius:50%;background:#fff}
.f-head{font-size:16px;color:#fff;font-weight:500}
.f-list{list-style:none;font-size:12px;color:#d9d3ec;line-height:32px}
.f-row{display:flex;gap:14px;align-items:flex-start;font-size:12px;color:#d9d3ec;line-height:18px;position:absolute;left:862px}
.f-row svg{width:18px;height:18px;flex:none}
.copy{top:5114px;font-size:11px;color:#d9d3ec}
</style>
</head>
<body>

<!-- Header -->
<svg class="abs hero-bg" viewBox="0 0 1200 660" aria-hidden="true">
  <defs><linearGradient id="heroGrad" x1="0" y1="0" x2="0" y2="1">
    <stop offset="0" stop-color="#4a1a7c"/><stop offset=".6" stop-color="#2f1560"/><stop offset="1" stop-color="#1f0f44"/>
  </linearGradient></defs>
  <path d="M0 0H1200V470C1140 560 1060 640 880 600 720 566 600 560 420 630 300 676 180 640 120 540 80 470 40 440 0 450Z" fill="url(#heroGrad)"/>
</svg>
<div class="abs logo">NORTHGRID</div>
<nav class="abs nav"><span>Home</span><span>About</span><span>Services</span><span>Portfolios</span><span>Team</span><span>Blog</span><span>Contact</span></nav>
<h1 class="abs hero-title">We Are Here, To Help Your Startup Business</h1>
<p class="abs hero-text">Data analytics software and expert services that turn your raw business data into clear, confident decisions.</p>
<div class="btn" style="left:174px;top:372px;width:130px">Get Start</div>
<div class="art" role="img" aria-label="Isometric illustration of a data center with analysts at desks" style="left:680px;top:100px;width:390px;height:330px;background:linear-gradient(135deg,#5a4fc0,#3b47a8 50%,#6a3a9c)"></div>

<!-- About -->
<div class="art" role="img" aria-label="Laptop with analytics charts and pie chart illustration" style="left:180px;top:720px;width:360px;height:380px;border-radius:50%;background:radial-gradient(circle,#4f46b8,#2a1f66 60%,var(--bg) 75%)"></div>
<div class="abs eyebrow" style="left:584px;top:784px">Who we are</div>
<h2 class="abs h-sec" style="left:584px;top:822px;width:440px">We Provide Additional Services That Will Grow Your Business</h2>
<p class="abs body-p" style="left:584px;top:910px;width:450px">Our analytics platform gathers data from every source you run, cleans it and shapes it into live dashboards, forecasts and reports. Alongside the software, our consultants plan, build and support the data work with your team, so insight reaches the people who need it and shows up in results you can measure.</p>
<div class="abs play" style="left:584px;top:1022px"><i></i>See How We Work</div>

<!-- Technology solution -->
<svg class="abs" style="left:760px;top:1160px" width="440" height="490" viewBox="0 0 440 490" aria-hidden="true">
  <path d="M140 20C230-10 340 10 440 30V490C360 470 260 440 170 450 60 460 0 380 20 300 40 220 40 60 140 20Z" fill="var(--blob)"/>
</svg>
<h2 class="abs h-sec" style="left:174px;top:1270px;width:420px">Perfect Technologynsolution For All Medium Business</h2>
<p class="abs body-p" style="left:174px;top:1360px;width:450px">From first data audit to daily reporting, we give medium businesses the same analytics depth as large firms. Our tools connect to your systems in days, and our professional services team trains your staff, tunes your models and keeps every dashboard accurate as your business grows and changes.</p>
<div class="abs check" style="left:174px;top:1474px"><svg viewBox="0 0 14 14"><circle cx="7" cy="7" r="6" fill="none" stroke="#d44ef0" stroke-width="1.3"/><path d="M4 7l2 2 4-4" fill="none" stroke="#d44ef0" stroke-width="1.3"/></svg>Expert Team Member</div>
<div class="abs check" style="left:392px;top:1474px"><svg viewBox="0 0 14 14"><circle cx="7" cy="7" r="6" fill="none" stroke="#d44ef0" stroke-width="1.3"/><path d="M4 7l2 2 4-4" fill="none" stroke="#d44ef0" stroke-width="1.3"/></svg>Time Management</div>
<div class="abs check" style="left:174px;top:1510px"><svg viewBox="0 0 14 14"><circle cx="7" cy="7" r="6" fill="none" stroke="#d44ef0" stroke-width="1.3"/><path d="M4 7l2 2 4-4" fill="none" stroke="#d44ef0" stroke-width="1.3"/></svg>Work Dedication</div>
<div class="abs check" style="left:392px;top:1510px"><svg viewBox="0 0 14 14"><circle cx="7" cy="7" r="6" fill="none" stroke="#d44ef0" stroke-width="1.3"/><path d="M4 7l2 2 4-4" fill="none" stroke="#d44ef0" stroke-width="1.3"/></svg>Faster Enrollments</div>
<div class="btn pink" style="left:174px;top:1546px;width:166px">Discover More</div>
<div class="art" role="img" aria-label="Two people working with large floating dashboard screens" style="left:690px;top:1260px;width:340px;height:280px;background:linear-gradient(135deg,#4d55c8,#3a2f96 50%,#5a79b8)"></div>

<!-- Services -->
<h2 class="abs center h-sec" style="top:1736px">We Provide IT &amp; Business Solutions</h2>
<p class="abs center body-p" style="top:1780px">Analytics software and hands-on professional services, built for companies<br>that want every decision backed by reliable data</p>

<div class="card" style="left:172px;top:1848px"><div class="ic" role="img" aria-label="Data analytics illustration"></div><h3>Data Analytics</h3><p>Live dashboards and forecasts built on all of your data</p><span>READ MORE</span></div>
<div class="card" style="left:465px;top:1848px"><div class="ic" role="img" aria-label="Software development illustration"></div><h3>Software Development</h3><p>Custom data pipelines and apps shaped around your needs</p><span>READ MORE</span></div>
<div class="card" style="left:758px;top:1848px"><div class="ic" role="img" aria-label="Data technology illustration"></div><h3>Data Technology</h3><p>Secure cloud warehouses that scale as your data grows</p><span>READ MORE</span></div>
<div class="card" style="left:172px;top:2174px"><div class="ic" role="img" aria-label="Professional services illustration"></div><h3>Professional Services</h3><p>Consultants who plan, deploy and support your analytics</p><span>READ MORE</span></div>
<div class="card" style="left:465px;top:2174px"><div class="ic" role="img" aria-label="Data strategy illustration"></div><h3>Data Strategy</h3><p>Clear roadmaps that link data work to business goals</p><span>READ MORE</span></div>
<div class="card" style="left:758px;top:2174px"><div class="ic" role="img" aria-label="Visual dashboards illustration"></div><h3>Visual Dashboards</h3><p>Readable reports that every team can act on each day</p><span>READ MORE</span></div>
<div class="btn pink" style="left:534px;top:2506px;width:124px">View All</div>

<!-- Stats -->
<div class="abs stats">
  <div class="stat" style="left:12px"><b>2,531</b><small>Project Finished</small></div>
  <div class="stat" style="left:228px"><b>15+</b><small>Years Experience</small></div>
  <div class="stat" style="left:442px"><b>280</b><small>Happy Clients</small></div>
  <div class="stat" style="left:648px"><b>3,587</b><small>Recognition</small></div>
</div>
<div class="art" role="img" aria-label="Rocket illustration" style="left:132px;top:2610px;width:130px;height:130px;border-radius:50%;background:linear-gradient(135deg,#ffb347,#f26b3a 50%,#5a8df0)"></div>
<div class="art" role="img" aria-label="Person turning large gears illustration" style="left:880px;top:2770px;width:190px;height:100px;background:linear-gradient(135deg,#3d5cf0,#2233a8 60%,#f08a6a)"></div>

<!-- Technology updates -->
<div class="art" role="img" aria-label="Faint dotted network pattern" style="left:880px;top:2930px;width:320px;height:500px;border-radius:0;background:radial-gradient(circle at 70% 50%,#3a1a5e,var(--bg) 70%)"></div>
<h2 class="abs center h-sec" style="top:2938px">Technology Updates</h2>
<article class="post" style="left:172px"><div class="img" role="img" aria-label="Dashboard screens with plants illustration" style="background:#4f7a6c"></div><div class="meta"><span><i></i>Lena Brooks</span><span>April 30, 2023</span></div><h3>Lorem Ipsum available, but the majority have suffered alteration</h3></article>
<article class="post" style="left:465px"><div class="img" role="img" aria-label="Data funnel with charts illustration" style="background:#4a4578"></div><div class="meta"><span><i></i>Mira Holt</span><span>June 13, 2023</span></div><h3>Lorem Ipsum available, but the majority have suffered alteration</h3></article>
<article class="post" style="left:758px"><div class="img" role="img" aria-label="People on a large laptop with charts illustration" style="background:#3c7f8c"></div><div class="meta"><span><i></i>Owen Pratt</span><span>March 24, 2023</span></div><h3>Lorem Ipsum available, but the majority have suffered alteration</h3></article>
<div class="abs center dots" style="top:3386px"><i style="width:14px;border-radius:3px;height:3px" class="on"></i><i style="height:3px;border-radius:2px;width:10px"></i><i style="height:3px;border-radius:2px;width:10px"></i></div>

<!-- Contact form -->
<svg class="abs" style="left:0;top:3470px" width="1200" height="480" viewBox="0 0 1200 480" aria-hidden="true">
  <defs><linearGradient id="formGrad" x1="0" y1="0" x2="0" y2="1"><stop offset="0" stop-color="#351a66"/><stop offset="1" stop-color="#170c33"/></linearGradient></defs>
  <path d="M0 60C120 10 240 30 360 80 480 130 600 20 760 30 900 40 1050 80 1200 40V480H0Z" fill="url(#formGrad)"/>
</svg>
<div class="art" role="img" aria-label="Team collaborating around a large website screen" style="left:170px;top:3560px;width:380px;height:260px;background:linear-gradient(135deg,#4b7fb8,#4a4fb8 50%,#a04f88)"></div>
<h2 class="abs h-sec" style="left:734px;top:3518px;font-weight:600">GET IN TOUCH</h2>
<div class="field" style="left:616px;top:3588px;width:196px">Name</div>
<div class="field" style="left:832px;top:3588px;width:196px">Phone</div>
<div class="field" style="left:616px;top:3660px;width:412px">Email</div>
<div class="field" style="left:616px;top:3734px;width:412px;padding-bottom:52px">Message</div>
<div class="btn" style="left:760px;top:3832px;width:116px">Submit</div>

<!-- Testimonials -->
<svg class="abs" style="left:0;top:3920px" width="700" height="420" viewBox="0 0 700 420" aria-hidden="true">
  <path d="M0 60C100 0 220 20 300 80 380 140 560 120 640 200 700 260 640 380 520 400 380 420 200 380 0 400Z" fill="var(--blob)"/>
</svg>
<div class="art" role="img" aria-label="Person working on a laptop on a sofa with video call screens" style="left:170px;top:4020px;width:430px;height:290px;background:linear-gradient(135deg,#3d5a8c,#c07a2a 55%,#4a55b8)"></div>
<h2 class="abs h-sec" style="left:720px;top:4050px">Words From Our Clients</h2>
<svg class="abs" style="left:666px;top:4128px" width="44" height="36" viewBox="0 0 44 36" aria-hidden="true"><path d="M0 36V20C0 8 8 2 18 0v7c-6 2-9 6-9 11h9v18zM24 36V20C24 8 32 2 42 0v7c-6 2-9 6-9 11h9v18z" fill="#7a3a8e"/></svg>
<p class="abs body-p" style="left:712px;top:4132px;width:316px;font-style:italic">"Fusce at nisi sed sapien volutpat malesuada. All the Lorem Ipsum genchunks as dolor sit amet consectetur lorem ipsum dolor sit amet Fusce at nisi sed sapien volutpat malesuada. Lorem ipsum dolor sit amet Fusce vel scelerisque erat facilisis."</p>
<div class="abs" style="left:712px;top:4250px;width:32px;height:32px;border-radius:50%;background:#4a3e75"></div>
<div class="abs" style="left:766px;top:4248px;font-size:11px;color:var(--accent-soft);font-weight:600">Rosa Vance</div>
<div class="abs" style="left:766px;top:4266px;font-size:11px;color:var(--text)">Graphic Designer</div>
<div class="abs dots" style="left:822px;top:4300px"><i class="on"></i><i></i><i></i></div>

<!-- Call to action -->
<h2 class="abs h-sec" style="left:174px;top:4500px;width:440px">Sounds Like Datavine Might Be The Right Choice For Your Business?</h2>
<p class="abs" style="left:174px;top:4578px;font-size:11px;color:var(--text)">Check Ranking Reports Via Our Web App. Contact Us Today!</p>
<div class="abs" style="left:256px;top:4612px;font-size:24px;font-weight:600;color:var(--accent)">+1 (555) 014-2290</div>
<div class="btn" style="left:296px;top:4666px;width:130px">Contact Us</div>
<div class="art" role="img" aria-label="Two people planning routes beside a large phone with map" style="left:680px;top:4440px;width:360px;height:310px;background:linear-gradient(135deg,#4a5a9c,#3f46a8 50%,#9a6a5a)"></div>

<!-- Footer -->
<svg class="abs footer-bg" viewBox="0 0 1200 397" aria-hidden="true">
  <path d="M0 40C200 70 380 20 560 60 760 100 960 0 1200 30V397H0Z" fill="var(--footer)"/>
</svg>
<div class="abs f-logo">NORTHGRID</div>
<p class="abs f-text">Data analytics software and professional services for growing companies</p>
<div class="abs social"><i></i><i></i><i></i><i></i></div>
<div class="abs f-head" style="left:576px;top:4920px">Quick Links</div>
<ul class="abs f-list" style="left:576px;top:4970px"><li>Home</li><li>About Us</li><li>Services</li><li>Contact Us</li></ul>
<div class="abs f-head" style="left:862px;top:4920px">Contact Us</div>
<div class="f-row" style="top:4976px"><svg viewBox="0 0 18 18"><circle cx="9" cy="9" r="8" fill="none" stroke="#fff"/><path d="M9 4a3 3 0 0 1 3 3c0 2.5-3 6-3 6s-3-3.5-3-6a3 3 0 0 1 3-3z" fill="#fff"/></svg><span>48 Harbor Lane, Eastport<br>4021, Northland</span></div>
<div class="f-row" style="top:5032px"><svg viewBox="0 0 18 18"><circle cx="9" cy="9" r="8" fill="none" stroke="#fff"/><path d="M6 5l2 0 1 2-1 1c.5 1 1.5 2 2.5 2.5l1-1 2 1v2c-4 0-7.5-3.5-7.5-7.5z" fill="#fff"/></svg><span>+1 (555) 014-2291</span></div>
<div class="f-row" style="top:5070px"><svg viewBox="0 0 18 18"><circle cx="9" cy="9" r="8" fill="none" stroke="#fff"/><rect x="5" y="6" width="8" height="6" fill="none" stroke="#fff"/><path d="M5 6l4 3 4-3" fill="none" stroke="#fff"/></svg><span>hello@northgrid.io</span></div>
<div class="abs center copy">2023 NORTHGRID. All Rights Reserved.</div>

</body>
</html>
```